Business Card Design

We need a business card design that can also be aplied for postcards. We are a small indie record company that also do consulting, and development of independat artitst . I already have the name and the basic idea of what i am looking for but i am open to any suggestion.
Info for the card
Name of the company : Velmora Records
NAME : Tomas Invaldi
PHONE : 208-5536142
EMAIL : hello@velmorarecords.example
WEB: www.velmorarecords.example
Target Market(s)
Male - Female independent musicians ages 18 to 45
Industry/Entity Type
Record Company
Contact Information for Business Card
Independant records company that also works in consulting for music business models for independent artists
Look and feel
Each slider illustrates characteristics of the customer's brand and the style your logo design should communicate.

```html
<!DOCTYPE html>
<html lang="en">
<head>
<meta charset="utf-8">
<title>Velmora Records – Business Card</title>
<link href="https://fonts.googleapis.com/css2?family=Questrial&family=Open+Sans:wght@400;700&display=swap" rel="stylesheet">
<style>
  :root {
    --paper: #ffffff;
    --ink: #0a0a0a;
    --label-grey: #5a5a5a;
    --disc-grey: #3d3d3d;
    --faint-grey: #4a4a4a;
    --edge: #cfcfcf;
    --text-light: #ffffff;
  }
  html, body {
    margin: 0;
    width: 1200px;
    height: 900px;
    overflow: hidden;
    background: var(--paper);
  }
  .canvas {
    position: relative;
    width: 1200px;
    height: 900px;
  }
  .card {
    position: absolute;
    left: 250px;
    width: 700px;
    height: 400px;
    display: block;
  }
  .card--front { top: 40px; outline: 1px solid var(--edge); }
  .card--back { top: 470px; }
  .brand-name { font-family: "Questrial", sans-serif; }
  .person-name { font-family: "Open Sans", sans-serif; font-weight: 700; }
  .person-role, .contact-line { font-family: "Open Sans", sans-serif; font-weight: 400; }
</style>
</head>
<body>
<main class="canvas">

  <!-- Front of the card -->
  <svg class="card card--front" viewBox="0 0 700 400" aria-label="Business card front">
    <defs>
      <clipPath id="front-clip"><rect width="700" height="400"/></clipPath>
    </defs>
    <rect class="card-face" width="700" height="400" fill="var(--paper)"/>
    <g clip-path="url(#front-clip)">
      <circle class="record-disc" cx="320" cy="440" r="300" fill="var(--ink)"/>
      <circle class="record-label" cx="320" cy="440" r="170" fill="var(--label-grey)"/>
      <circle class="record-hole" cx="320" cy="440" r="62" fill="var(--paper)"/>
    </g>

    <g class="brand">
      <circle class="brand-dot" cx="345" cy="84" r="18" fill="var(--ink)"/>
      <text class="brand-name" x="374" y="98" font-size="38" fill="var(--ink)">Velmora Records</text>
    </g>

    <g class="person" text-anchor="middle">
      <text class="person-name" x="320" y="190" font-size="26" fill="var(--text-light)">TOMAS INVALDI</text>
      <text class="person-role" x="320" y="214" font-size="14" fill="var(--text-light)">Director</text>
    </g>

    <g class="contact" text-anchor="middle" fill="var(--text-light)">
      <text class="contact-line" x="320" y="310" font-size="15">208-5536142</text>
      <text class="contact-line" x="320" y="332" font-size="15">hello@velmorarecords.example</text>
      <text class="contact-line" x="320" y="354" font-size="15">www.velmorarecords.example</text>
    </g>
  </svg>

  <!-- Back of the card -->
  <svg class="card card--back" viewBox="0 0 700 400" aria-label="Business card back">
    <defs>
      <clipPath id="back-clip"><rect width="700" height="400"/></clipPath>
    </defs>
    <rect class="card-face" width="700" height="400" fill="var(--ink)"/>
    <g class="record record--faint" clip-path="url(#back-clip)">
      <circle class="record-disc" cx="300" cy="20" r="250" fill="var(--disc-grey)"/>
      <circle class="record-label" cx="300" cy="20" r="150" fill="var(--label-grey)"/>
      <circle class="record-hole" cx="300" cy="20" r="55" fill="var(--ink)"/>
    </g>
    <g class="brand brand--faint">
      <circle class="brand-dot" cx="128" cy="318" r="22" fill="var(--faint-grey)"/>
      <text class="brand-name" x="162" y="334" font-size="44" fill="var(--faint-grey)">Velmora Records</text>
    </g>
  </svg>

</main>
</body>
</html>
```